Food broker, trader, wholesaler, liquidator looking for a 5 pages website

Looking for a 5 pages website design. We are food brokers, traders, wholesaler and closeout buyer working with manufacturers, distributors, importers sell to retailers, food service operators and industrial (ingredients). We help market their products. We are a resource for those who need a solution in the distribution/selling/placement of food on the shelves, kitchens and pantries. Whether we open new accounts with new products or sell short dated inventory, we know where to go and get results.

Target Market(s)

Food manufacturers, food distributors, food brokers

Coding

Coded - Design and coding required

Number of Pages Required

4 page

Font styles to use
Serif

Requirements
Must have
• Food-food production-warehouse-Food packaging-people meeting-trucks-supermarket shelves-

```html
<!DOCTYPE html>
<html lang="en">
<head>
<meta charset="utf-8">
<title>Harbor Provisions — Food Broker &amp; Wholesaler</title>
<link href="https://fonts.googleapis.com/css2?family=Poppins:wght@400;500;600;700&family=Great+Vibes&family=Libre+Baskerville:wght@700&family=Playfair+Display:wght@900&display=swap" rel="stylesheet">
<style>
:root{
  --navy:#0e1a6b;
  --royal:#2a44a6;
  --ink:#222;
  --muted:#555;
  --grey:#dcdcdc;
  --white:#fff;
  --black:#000;
}
*{box-sizing:border-box;margin:0;padding:0}
html,body{width:1200px;height:2875px;overflow:hidden;background:var(--white)}
body{font-family:"Poppins",sans-serif;color:var(--ink);position:relative}
.abs{position:absolute}
.script{font-family:"Great Vibes",cursive;font-weight:400}
.section-title{position:absolute;left:0;width:1200px;text-align:center;font-family:"Great Vibes",cursive;font-size:44px;color:var(--navy)}
.section-lead{position:absolute;left:0;width:1200px;text-align:center;font-size:9.5px;line-height:15px;color:var(--ink)}

/* header */
.header{top:0;left:0;width:1200px;height:114px}
.social-top{top:46px;left:234px;display:flex;gap:7px}
.social-top span{width:18px;height:18px;border-radius:50%;background:#e8edf6;display:block}
.brand{top:14px;left:520px;width:160px;text-align:center}
.brand-mark{width:84px;height:62px;border-radius:50%;background:var(--navy);margin:0 auto}
.brand-name{font-family:"Libre Baskerville",serif;font-weight:700;font-size:10.5px;color:var(--navy);margin-top:6px;letter-spacing:.2px}
.login{top:31px;left:861px;width:105px;height:25px;background:var(--navy);color:var(--white);font-size:7.5px;display:flex;align-items:center}
.login i{width:24px;height:25px;border-right:1px solid #3a4690;display:flex;align-items:center;justify-content:center}
.login b{font-weight:500;padding-left:9px}
.phone{top:68px;left:820px;width:146px;text-align:right;font-weight:600;font-size:16px;color:var(--navy)}
.nav{top:114px;left:0;width:1200px;height:35px;background:var(--navy);display:flex;justify-content:center;align-items:center}
.nav a{color:var(--white);font-size:8.5px;font-weight:600;text-decoration:none;padding:0 14px;border-left:1px solid #3c4690}
.nav a:first-child{border-left:none}

/* hero */
.hero{top:149px;left:0;width:1200px;height:410px;background:linear-gradient(90deg,#b9a06a 0%,#c9b796 25%,#d8d0c0 45%,#c8b89a 65%,#a99670 85%,#c7cdb2 100%)}
.hero-shade{top:149px;left:0;width:1200px;height:410px;background:rgba(40,40,40,.22)}
.hero-kicker{top:232px;left:0;width:1200px;text-align:center;font-family:"Great Vibes",cursive;font-size:34px;color:var(--white)}
.hero-title{top:275px;left:0;width:1200px;text-align:center;font-family:"Playfair Display",serif;font-weight:900;font-size:54px;line-height:48px;color:#f3f3f3;letter-spacing:2px}
.arrow{top:322px;width:20px;height:30px}
.dots{top:482px;left:558px;display:flex;gap:4px;align-items:center}
.dots span{width:8px;height:8px;border-radius:50%;background:rgba(255,255,255,.45)}
.dots .on{width:11px;height:11px;border:2px solid var(--white);background:transparent}
.hero-edge{top:490px;left:0}

/* about */
.about-photo{top:605px;left:230px;width:302px;height:302px;border-radius:50%;background:radial-gradient(circle at 50% 40%,#e1b98f,#c88b44 60%,#9a6330);border:5px solid #e4e6ee}
.about-title{top:630px;left:563px;font-size:40px;color:var(--navy)}
.about-copy{top:686px;left:565px;width:402px;font-size:9.3px;line-height:15px}
.about-copy p{margin-bottom:15px}
.btn{display:flex;align-items:center;justify-content:center;gap:10px;background:var(--navy);color:var(--white);font-weight:600;font-size:8.5px;border-radius:16px}
.learn{top:834px;left:566px;width:106px;height:31px}

/* services */
.services-bg{top:955px;left:0}
.services .section-title{color:var(--white);top:1010px}
.services .section-lead{color:var(--white);top:1070px}
.cards{top:1137px;left:234px;display:flex;gap:19px}
.card{width:169px;height:184px;background:var(--white);border-radius:4px;box-shadow:0 2px 6px rgba(0,0,0,.25);text-align:center;padding-top:22px}
.card-icon{width:50px;height:50px;border-radius:50%;background:var(--navy);margin:0 auto;display:flex;align-items:center;justify-content:center}
.card h3{font-size:11.5px;font-weight:600;margin:12px 0 7px;color:var(--ink)}
.card p{font-size:8.6px;line-height:15px;padding:0 12px;color:var(--ink)}

/* category */
.category .section-title{top:1445px}
.category .section-lead{top:1504px}
.tiles{top:1563px;left:234px;display:grid;grid-template-columns:repeat(3,231px);grid-auto-rows:232px;column-gap:19px;row-gap:19px}
.tile{position:relative;display:flex;align-items:center;justify-content:center}
.tile span{color:var(--white);font-weight:600;font-size:13.5px;text-shadow:0 1px 3px rgba(0,0,0,.5);position:relative}
.t1{background:linear-gradient(160deg,#8a7866,#5c4a3c 60%,#3a2a22)}
.t2{background:linear-gradient(180deg,#6d5d55,#8d8080 50%,#9a8a88)}
.t3{background:linear-gradient(160deg,#8a3a3a,#a04848 45%,#b99a5a)}
.t4{background:linear-gradient(160deg,#8f8a84,#6c5e54 55%,#8a7058)}
.t5{background:linear-gradient(180deg,#7c8890,#6a7478 50%,#5a6468)}
.t6{background:linear-gradient(160deg,#a8b2a0,#6f8a6c 55%,#3f5e48)}

/* partners */
.partners .section-title{top:2090px}
.partners .section-lead{top:2150px}
.badges{top:2220px;left:234px;display:grid;grid-template-columns:repeat(5,132px);grid-auto-rows:84px;column-gap:16px;row-gap:22px}
.badge{background:#eef0f6;border-radius:8px}
.badge.round{border-radius:50%;width:84px;margin:0 auto}

/* footer */
.footer-bg{top:2480px;left:0}
.footer{color:var(--white)}
.f-brand{top:2560px;left:234px;width:190px}
.f-mark{width:84px;height:62px;border-radius:50%;background:var(--navy);margin-left:30px}
.f-name{font-family:"Libre Baskerville",serif;font-weight:700;font-size:11px;margin:8px 0 12px}
.f-about{font-size:9px;line-height:15px}
.f-social{top:2720px;left:234px;display:flex;gap:8px}
.f-social span{width:26px;height:26px;border-radius:50%;background:#2a2a2a;display:block}
.f-col h4{font-size:10px;font-weight:600;letter-spacing:.3px;margin-bottom:16px}
.f-col li{list-style:none;font-size:9px;margin-bottom:10.5px}
.f-info{top:2583px;left:455px}
.f-contact{top:2583px;left:608px;width:180px}
.f-contact li{display:flex;gap:8px;line-height:15px;margin-bottom:10px}
.f-form{top:2583px;left:810px;width:156px}
.field{height:24px;border:1px solid #ccc;border-radius:2px;font-size:7.5px;padding:6px 8px;margin-bottom:7px}
.field.area{height:48px}
.send{width:72px;height:25px;background:var(--navy);border-radius:2px;font-size:8.5px;font-weight:600;display:flex;align-items:center;justify-content:center;margin-top:11px}
.f-photo{top:2640px;left:960px;width:240px;height:235px;background:radial-gradient(ellipse at 70% 65%,#8a1a12,#4a0d08 45%,#000 75%)}
.copyright{top:2830px;left:0;width:1200px;text-align:center;font-size:9px;color:#bbb}
</style>
</head>
<body>

<header class="header abs">
  <div class="social-top abs"><span></span><span></span><span></span><span></span><span></span></div>
  <div class="brand abs"><div class="brand-mark"></div><div class="brand-name">HARBOR PROVISIONS</div></div>
  <div class="login abs"><i><svg width="9" height="9" viewBox="0 0 10 10" fill="none" stroke="#fff"><circle cx="5" cy="3" r="2"/><path d="M1 9c0-2 2-3 4-3s4 1 4 3"/></svg></i><b>LOGIN / REGISTER</b></div>
  <div class="phone abs">0(800) 555 01 42</div>
</header>
<nav class="nav abs"><a>ABOUT US</a><a>WHAT WE DO</a><a>CONTACT</a><a>GIVING BACK</a></nav>

<section class="hero-wrap">
  <div class="hero abs" role="img" aria-label="Photo of a shopper reaching for products on supermarket shelves"></div>
  <div class="hero-shade abs"></div>
  <div class="hero-kicker abs">For Your Health &amp; Happiness</div>
  <div class="hero-title abs">SUPER<br>MARKET</div>
  <svg class="arrow abs" style="left:54px" viewBox="0 0 20 30"><path d="M14 4L4 15l10 11" fill="none" stroke="#fff" stroke-width="3"/></svg>
  <svg class="arrow abs" style="left:1112px" viewBox="0 0 20 30"><path d="M6 4l10 11-10 11" fill="none" stroke="#fff" stroke-width="3"/></svg>
  <div class="dots abs"><span></span><span></span><span></span><span></span><span></span><span class="on"></span><span></span></div>
  <svg class="hero-edge abs" width="1200" height="70" viewBox="0 0 1200 70">
    <polygon points="0,20 320,65 733,42 1200,58 1200,70 0,70" fill="#fff"/>
    <polygon points="0,15 0,20 320,65 733,42 1200,58 1200,45 733,22" fill="#dedede"/>
  </svg>
</section>

<section class="about">
  <div class="about-photo abs" role="img" aria-label="Portrait photo of a smiling shop assistant in an apron"></div>
  <h2 class="about-title abs script">About Us</h2>
  <div class="about-copy abs">
    <p>Harbor Provisions works with food manufacturers, brand owners, distributors and wholesalers market their products.</p>
    <p>Retail, Food Service and Industrial ingredients.</p>
    <p>Founded in 2008, Harbor Provisions started with the distribution of gluten free products understanding the need to provide access to unique flavors and products forthe celiac consumers. From this, we expanded into deli, dairy, groceries, frozen and beverages.</p>
  </div>
  <div class="btn learn abs">LEARN MORE <svg width="9" height="7" viewBox="0 0 9 7"><path d="M0 3.5h7M5 1l2.5 2.5L5 6" fill="none" stroke="#fff"/></svg></div>
</section>

<section class="services">
  <svg class="services-bg abs" width="1200" height="455" viewBox="0 0 1200 455">
    <polygon points="0,30 0,60 296,8 1200,47 1200,5 880,35 296,8" fill="#dedede"/>
    <polygon points="0,58 296,8 1200,52 1200,432 900,410 740,405 0,408" fill="#2a44a6"/>
    <polygon points="0,408 740,405 1200,432 1200,452 740,405 300,452 0,420" fill="#dedede"/>
    <polygon points="0,408 740,405 300,452" fill="#2a44a6"/>
  </svg>
  <h2 class="section-title">Our Services</h2>
  <p class="section-lead">Lorem ipsum dolor sit amet, consectetur adipiscing elit. Mauris ultricies non diam in hendrerit.<br>Sed quis risus non eros tempor consectetur.</p>
  <div class="cards abs">
    <div class="card"><div class="card-icon"><svg width="22" height="22" viewBox="0 0 22 22" fill="none" stroke="#fff" stroke-width="1.3"><circle cx="7" cy="5" r="2.5"/><path d="M3 20v-7c0-2 2-3 4-3s4 1 4 3v7M13 12h6v8h-6z"/></svg></div><h3>Food Broker</h3><p>Lorem ipsum dolor sit amet, consectetur adipiscing elit. Mauris ultricies non diam in hendrerit. Sed quis risus non eros.</p></div>
    <div class="card"><div class="card-icon"><svg width="22" height="22" viewBox="0 0 22 22" fill="none" stroke="#fff" stroke-width="1.3"><path d="M3 8l2-5h12l2 5zM4 8v11h14V8M8 19v-6h6v6"/></svg></div><h3>Trader</h3><p>Lorem ipsum dolor sit amet, consectetur adipiscing elit. Mauris ultricies non diam in hendrerit. Sed quis risus non eros.</p></div>
    <div class="card"><div class="card-icon"><svg width="22" height="22" viewBox="0 0 22 22" fill="none" stroke="#fff" stroke-width="1.3"><path d="M2 8l9-5 9 5v12H2zM6 20v-8h10v8M6 15h10"/></svg></div><h3>Wholesaler</h3><p>Lorem ipsum dolor sit amet, consectetur adipiscing elit. Mauris ultricies non diam in hendrerit. Sed quis risus non eros.</p></div>
    <div class="card"><div class="card-icon"><svg width="22" height="22" viewBox="0 0 22 22" fill="none" stroke="#fff" stroke-width="1.3"><path d="M4 8h14v12H4zM7 8V5h8v3M8 12h6v5H8z"/></svg></div><h3>Closeout</h3><p>Lorem ipsum dolor sit amet, consectetur adipiscing elit. Mauris ultricies non diam in hendrerit. Sed quis risus non eros.</p></div>
  </div>
</section>

<section class="category">
  <h2 class="section-title">Our Category</h2>
  <p class="section-lead">Lorem ipsum dolor sit amet, consectetur adipiscing elit. Mauris ultricies non diam in hendrerit.<br>Sed quis risus non eros tempor consectetur.</p>
  <div class="tiles abs">
    <div class="tile t1" role="img" aria-label="Photo of a chef seasoning a plated dish"><span>FOOD PRODUCTION</span></div>
    <div class="tile t2" role="img" aria-label="Photo of warehouse aisles with stocked racks"><span>WAREHOUSE</span></div>
    <div class="tile t3" role="img" aria-label="Photo of fruit in clear plastic packaging"><span>FOOD PACKAGING</span></div>
    <div class="tile t4" role="img" aria-label="Photo of people meeting around a table with food"><span>PEOPLE MEETING</span></div>
    <div class="tile t5" role="img" aria-label="Photo of a vintage food truck"><span>TRUCKS</span></div>
    <div class="tile t6" role="img" aria-label="Photo of a shopper at supermarket shelves"><span>SUPERMARKET SHELVES</span></div>
  </div>
</section>

<section class="partners">
  <h2 class="section-title">Our Partners</h2>
  <p class="section-lead">Lorem ipsum dolor sit amet, consectetur adipiscing elit. Mauris ultricies non diam in hendrerit.<br>Sed quis risus non eros tempor consectetur.</p>
  <div class="badges abs">
    <div class="badge"></div><div class="badge"></div><div class="badge round"></div><div class="badge"></div><div class="badge"></div>
    <div class="badge round" style="width:120px"></div><div class="badge"></div><div class="badge"></div><div class="badge"></div><div class="badge"></div>
  </div>
</section>

<footer class="footer">
  <svg class="footer-bg abs" width="1200" height="395" viewBox="0 0 1200 395">
    <rect x="0" y="30" width="1200" height="365" fill="#000"/>
    <polygon points="0,0 1200,0 1200,30 880,55 300,30 0,50" fill="#0e1a6b"/>
    <polygon points="300,30 880,55 1200,30 1200,60 880,55 0,60 0,50" fill="#000"/>
  </svg>
  <div class="f-photo abs" role="img" aria-label="Photo of red chili peppers in a bowl"></div>
  <div class="f-brand abs">
    <div class="f-mark"></div>
    <div class="f-name">HARBOR PROVISIONS</div>
    <p class="f-about">Harbor Provisions works with food manufacturers, brand owners, distributors and wholesalers market their products.</p>
  </div>
  <div class="f-social abs"><span></span><span></span><span></span><span></span><span></span></div>
  <div class="f-col f-info abs">
    <h4>INFORMATION</h4>
    <ul><li>New Customer Registration</li><li>Product Catalogue</li><li>Contact Us</li><li>Trading Conditions</li><li>Blog</li><li>Career</li></ul>
  </div>
  <div class="f-col f-contact abs">
    <h4>CONTACT INFO</h4>
    <ul>
      <li><svg width="10" height="10" viewBox="0 0 10 10"><path d="M2 1l2 2-1 1.5c.6 1.2 1.3 1.9 2.5 2.5L7 6l2 2-1.5 1.5C4 9 1 6 .5 2.5z" fill="#fff"/></svg>Call us: (866) 555-0199</li>
      <li><svg width="10" height="10" viewBox="0 0 10 10"><rect x=".5" y="2" width="9" height="6.5" fill="#fff"/><path d="M.5 2l4.5 3.5L9.5 2" fill="none" stroke="#000"/></svg>hello@harborprovisions.com</li>
      <li><svg width="10" height="13" viewBox="0 0 10 13"><path d="M5 0a4.5 4.5 0 014.5 4.5C9.5 8 5 13 5 13S.5 8 .5 4.5A4.5 4.5 0 015 0z" fill="#fff"/><circle cx="5" cy="4.5" r="1.6" fill="#000"/></svg>12 - C, 3rd Floor, Elm Court Apartments, Kent, UK.40BX112D.</li>
    </ul>
  </div>
  <div class="f-col f-form abs">
    <h4>CONTACT US</h4>
    <div class="field">Name*</div>
    <div class="field">Email*</div>
    <div class="field">Phone*</div>
    <div class="field area">Message</div>
    <div class="send">SEND</div>
  </div>
  <p class="copyright abs">Copyright © 2020 Harbor Provisions. All rights reserved.</p>
</footer>

</body>
</html>
```